Flyer-Design / Verodina
Zielgruppe
Licht zu verstehen und richtig einzusetzen ist ein wesentlicher Bestandteil, um die Wirkung von Architektur, Innenräumen und Landschaften zu unterstützen und zu steigern. Die harmonische Verschmelzung von moderner Architektur und akzentuiert eingesetztem Licht verleiht Innenräumen ihre eigene Note. Dieses Zusammenspiel erfordert über das Berechnen und die Leuchtenauswahl hinaus einen sehr sensiblen Umgang mit dem Medium Licht. Bei jeder Lichtplanung steht der Mensch mit seiner Wahrnehmung von Licht und Schatten im Mittelpunkt. Eine hochwertige Lichtplanung vom Fachmann verfolgt mit ihrem ganzheitlichen Ansatz daher den Anspruch Atmosphäre, Wohlbefinden und Orientierung zu schaffen und den beleuchteten Räumen Ausdruckskraft zu verleihen.
Aufgabenstellung
WIr möchten einen Flyer für unseren Laden der für den Kunden sehr ansprechend ist, im Bezug auf unserer Planungen und unseren Handel.
Wir möchten darauf eine Zusammenfassung unser Arbeit und unserer Portfolios sehen die dem Kunden sofort sagen was wir machen.

```html
<!DOCTYPE html>
<html lang="de">
<head>
<meta charset="utf-8">
<title>Verodina – Flyer</title>
<link rel="stylesheet" href="https://fonts.googleapis.com/css2?family=Arimo:wght@400&family=Quicksand:wght@400&display=swap">
<style>
  :root {
    --yellow: #fde400;
    --charcoal: #323538;
    --paper: #ffffff;
    --ink: #2b2b2b;
    --muted: #8d9093;
    --label: #1e1e1e;
  }
  html, body { margin: 0; padding: 0; overflow: hidden; background: var(--paper); }
  .canvas { width: 1200px; height: 1200px; overflow: hidden; background: var(--paper); }
  .canvas svg { display: block; }
  .piece-text { font-family: "Arimo", Helvetica, Arial, sans-serif; }
  .sheet-label { font-family: "Quicksand", "Century Gothic", sans-serif; font-size: 25px; fill: var(--label); }
  .fill-yellow { fill: var(--yellow); }
  .fill-charcoal { fill: var(--charcoal); }
  .fill-paper { fill: var(--paper); }
  .headline { font-size: 15px; fill: var(--yellow); }
  .body-copy { font-size: 7.4px; fill: var(--ink); }
  .claim { font-size: 27px; fill: var(--charcoal); }
  .claim-dark { font-size: 25px; fill: var(--charcoal); }
  .claim-light { font-size: 25px; fill: var(--paper); }
  .brand-name { font-size: 30px; fill: var(--paper); letter-spacing: 3px; }
  .brand-tag { font-size: 7.5px; fill: var(--muted); letter-spacing: 1px; }
  .contact { font-size: 9.5px; fill: var(--charcoal); }
  .bubble-text { font-size: 8.6px; fill: var(--ink); }
</style>
</head>
<body>
<div class="canvas">
<svg width="1200" height="1200" viewBox="0 0 1200 1200" class="piece-text" xmlns="http://www.w3.org/2000/svg">
  <defs>
    <filter id="panel-shadow" x="-5%" y="-5%" width="110%" height="110%">
      <feDropShadow dx="0" dy="2" stdDeviation="2" flood-opacity="0.3"/>
    </filter>
    <clipPath id="panel-clip"><rect x="0" y="0" width="225" height="476"/></clipPath>

    <linearGradient id="tone-dark" x1="0" y1="0" x2="0" y2="1"><stop offset="0" stop-color="#3b3d40"/><stop offset="1" stop-color="#252628"/></linearGradient>
    <linearGradient id="tone-white" x1="0" y1="0" x2="0" y2="1"><stop offset="0" stop-color="#ffffff"/><stop offset="1" stop-color="#f1f1f1"/></linearGradient>
    <radialGradient id="tone-grey" cx="0.5" cy="0.25" r="0.8"><stop offset="0" stop-color="#d6d6d8"/><stop offset="1" stop-color="#7b7c80"/></radialGradient>
    <linearGradient id="tone-light" x1="0" y1="0" x2="1" y2="1"><stop offset="0" stop-color="#e2e2e2"/><stop offset="1" stop-color="#b4b4b4"/></linearGradient>

    <g id="bubble">
      <circle cx="0" cy="0" r="42" class="fill-yellow"/>
      <text class="bubble-text" x="-24" y="-11">Lorem ipsum</text>
      <text class="bubble-text" x="-24" y="-1.4">dolor sit amet,</text>
      <text class="bubble-text" x="-24" y="8.2">consectetuer</text>
      <text class="bubble-text" x="-24" y="17.8">adipiscing elit.</text>
    </g>

    <!-- inner flap: white text column with yellow circle -->
    <g id="panel-flap">
      <rect x="0" y="0" width="225" height="476" class="fill-charcoal"/>
      <rect x="11" y="11" width="214" height="465" class="fill-paper"/>
      <g clip-path="url(#panel-clip)">
        <circle cx="83" cy="443" r="130" class="fill-yellow"/>
      </g>
      <text class="headline" x="19" y="37">Headline Headline</text>
      <g class="body-copy">
        <text x="19" y="87">Lorem ipsum dolor sit amet, consectetuer adipiscing</text>
        <text x="19" y="96.6">elit. Aenean commodo ligula eget dolor. Aenean massa.</text>
        <text x="19" y="106.2">Cum sociis natoque penatibus et magnis dis parturient</text>
        <text x="19" y="115.8">montes, nascetur ridiculus mus. Donec quam felis, ultri-</text>
        <text x="19" y="125.4">cies nec, pellentesque eu, pretium quis, sem.</text>
        <text x="19" y="145">Nulla consequat massa quis enim. Donec pede justo,</text>
        <text x="19" y="154.6">fringilla vel, aliquet nec, vulputate eget, arcu. In enim jus-</text>
        <text x="19" y="164.2">to, rhoncus ut, imperdiet a, venenatis vitae, justo. Nullam</text>
        <text x="19" y="173.8">dictum felis eu pede mollis pretium. Integer tincidunt.</text>
        <text x="19" y="183.4">Cras dapibus. Vivamus elementum semper nisi.</text>
        <text x="19" y="202.6">Aenean vulputate eleifend tellus. Aenean leo ligula,</text>
        <text x="19" y="212.2">porttitor eu, consequat vitae, eleifend ac, enim. Aliquam</text>
        <text x="19" y="221.8">lorem ante, dapibus in, viverra quis, feugiat a, tellus.</text>
        <text x="19" y="231.4">Phasellus viverra nulla ut metus varius laoreet.</text>
        <text x="19" y="250.7">Quisque rutrum. Aenean imperdiet.</text>
      </g>
      <text class="claim" x="19" y="402">bei uns finden</text>
      <text class="claim" x="19" y="433.5">Sie die richtige</text>
      <text class="claim" x="19" y="465">Leuchte</text>
    </g>

    <!-- back panel: contact details -->
    <g id="panel-back">
      <rect x="0" y="0" width="225" height="476" class="fill-charcoal"/>
      <g clip-path="url(#panel-clip)">
        <circle cx="225" cy="405" r="173" class="fill-yellow"/>
      </g>
      <g class="contact" text-anchor="end">
        <text x="214" y="373">verodina</text>
        <text x="214" y="384.6">Kastanienallee 17</text>
        <text x="214" y="396.2">54321 Feldbrunn</text>
        <text x="214" y="407.8">Tel: +49 1234-5678900</text>
        <text x="214" y="419.4">Email: info@verodina.de</text>
        <text x="214" y="431">www. verodina.de</text>
        <text x="214" y="453.6">Öffnungszeiten:</text>
        <text x="214" y="465.2">(Mo–Fr.) 8:00–17:00</text>
      </g>
    </g>

    <!-- front panel: title -->
    <g id="panel-front">
      <rect x="0" y="0" width="225" height="476" class="fill-charcoal"/>
      <g clip-path="url(#panel-clip)">
        <circle cx="0" cy="405" r="173" class="fill-yellow"/>
      </g>
      <text class="brand-name" x="205" y="80" text-anchor="end">VERODINA</text>
      <text class="brand-tag" x="103" y="95">Lichtberatung +</text>
      <text class="brand-tag" x="103" y="104">Fachhandel</text>
      <text class="claim-dark" x="149" y="335" text-anchor="end">wir machen</text>
      <text class="claim-light" x="209" y="335" text-anchor="end">licht</text>
    </g>
  </defs>

  <!-- Aussenseite -->
  <g class="spread-outside" transform="translate(29,23)" filter="url(#panel-shadow)">
    <use href="#panel-flap" x="0" y="0"/>
    <use href="#panel-back" x="224" y="0"/>
    <use href="#panel-front" x="449" y="0"/>
  </g>
  <text class="sheet-label" x="50" y="532">aussen</text>

  <!-- Titel -->
  <g class="single-title" transform="translate(725,23)" filter="url(#panel-shadow)">
    <use href="#panel-front"/>
  </g>
  <text class="sheet-label" x="731" y="532">Titel</text>

  <!-- Rückseite -->
  <g class="single-back" transform="translate(967,23)" filter="url(#panel-shadow)">
    <use href="#panel-back"/>
  </g>
  <text class="sheet-label" x="972" y="524">Rückseite</text>

  <!-- Innenseite -->
  <g class="spread-inside" transform="translate(29,592)" filter="url(#panel-shadow)">
    <rect x="0" y="0" width="674" height="476" class="fill-paper"/>
    <rect x="0" y="0" width="225" height="156" fill="url(#tone-dark)" role="img" aria-label="Foto: schwarze Pendelleuchte mit Halbkugelschirm vor dunklem Hintergrund"/>
    <rect x="225" y="0" width="224" height="156" fill="url(#tone-white)" role="img" aria-label="Foto: Kristall-Pendelleuchte vor weißem Hintergrund"/>
    <rect x="449" y="0" width="225" height="156" fill="url(#tone-white)" role="img" aria-label="Foto: Kristall-Pendelleuchte vor weißem Hintergrund"/>
    <rect x="0" y="160" width="225" height="156" fill="url(#tone-grey)" role="img" aria-label="Foto: dunkle Kugel-Wandleuchte an grauer Wand"/>
    <rect x="225" y="160" width="224" height="156" fill="url(#tone-grey)" role="img" aria-label="Foto: weiße Deckenleuchte an grauer Wand"/>
    <rect x="449" y="160" width="225" height="156" fill="url(#tone-grey)" role="img" aria-label="Foto: weiße Deckenleuchte an grauer Wand"/>
    <rect x="0" y="320" width="225" height="156" fill="url(#tone-light)" role="img" aria-label="Foto: schwarze Wandschale mit goldenem Inneren"/>
    <rect x="225" y="320" width="224" height="156" fill="url(#tone-dark)" role="img" aria-label="Foto: schwarze Pendelleuchte mit Halbkugelschirm"/>
    <rect x="449" y="320" width="225" height="156" fill="url(#tone-dark)" role="img" aria-label="Foto: schwarze Pendelleuchte mit Halbkugelschirm"/>
    <use href="#bubble" x="170" y="106"/>
    <use href="#bubble" x="394" y="53"/>
    <use href="#bubble" x="621" y="53"/>
    <use href="#bubble" x="52" y="271"/>
    <use href="#bubble" x="275" y="205"/>
    <use href="#bubble" x="501" y="205"/>
    <use href="#bubble" x="170" y="397"/>
    <use href="#bubble" x="394" y="423"/>
    <use href="#bubble" x="621" y="423"/>
  </g>
  <text class="sheet-label" x="38" y="1110">innen</text>

  <!-- einmal aufgeklappt -->
  <g class="spread-half-open" transform="translate(740,596)" filter="url(#panel-shadow)">
    <rect x="0" y="0" width="225" height="476" class="fill-paper"/>
    <rect x="0" y="0" width="225" height="156" fill="url(#tone-dark)" role="img" aria-label="Foto: schwarze Pendelleuchte mit Halbkugelschirm vor dunklem Hintergrund"/>
    <rect x="0" y="160" width="225" height="156" fill="url(#tone-grey)" role="img" aria-label="Foto: dunkle Kugel-Wandleuchte an grauer Wand"/>
    <rect x="0" y="320" width="225" height="156" fill="url(#tone-light)" role="img" aria-label="Foto: schwarze Wandschale mit goldenem Inneren"/>
    <use href="#bubble" x="172" y="124"/>
    <use href="#bubble" x="56" y="290"/>
    <use href="#bubble" x="172" y="420"/>
    <use href="#panel-flap" x="225" y="0"/>
  </g>
  <text class="sheet-label" x="765" y="1160">1x aufgeklappt</text>
</svg>
</div>
</body>
</html>
```